Rack Card for Charter Sail Boat business in SF Bay

We are in need of a rack card design to highlight the business to tourists and locals. 2 sided card 3.86" x 8.39" (full bleed)

We are looking for visually appleaing designs on the front and back but a little more detail on the back.

Use the info provided (text and info) on the website to include the 3 key services (Quick, 1/2 day, fullday) and aspects of the boat, location and other key info for customers (not prices). DO NOT INCLUDE ALL THIS TEXT please pick the elements you would like to fit your design and inform the customer as you would like about the business.

I can also provide photos directly from the video if you think those would fit your design. If video doesn't work on this upload you can view it at the website or facebook page (www.fb.com/tidewrenllc)

Now included a few video pictures in files for your use

Target Market(s)

Tourists and locals to san francisco east bay. 25 - 55 years old. Men and women.

Industry/Entity Type

Entertainment

Colors
0455a3
ec1f27
f3f1f8

Requirements
Must have
• Highlight services, key contact information (email, phone, website site), Visual impact
• 2-sided card - 3.86" x 8.39" (98 x 213 mm)
Nice to have
• facebook link, electric engine(green),

```html
<!DOCTYPE html>
<html lang="en">
<head>
<meta charset="utf-8">
<title>Tidewren Rack Card</title>
<link rel="stylesheet" href="https://fonts.googleapis.com/css2?family=Raleway:wght@300;400;700;800&family=Roboto+Condensed:wght@400;700&family=Oswald:wght@500&display=swap">
<style>
  :root {
    --navy: #0b2a73;
    --brand-blue: #0455a3;
    --headline-blue: #1a3f94;
    --brand-red: #ec1f27;
    --coral: #ef5a3a;
    --teal: #2aa3b5;
    --paper: #f3f1f8;
    --ink: #1c1f2a;
    --ink-soft: #2b2f3d;
    --stage: #000000;
  }
  * { margin: 0; padding: 0; box-sizing: border-box; }
  html, body { width: 1200px; height: 1200px; overflow: hidden; background: var(--stage); }
  .stage { position: relative; width: 1200px; height: 1200px; }

  .card { position: absolute; top: 138px; width: 426px; height: 941px; overflow: hidden; }
  .card--front { left: 172px; }
  .card--back { left: 635px; width: 424px; }

  /* FRONT */
  .front-scene {
    position: absolute; inset: 0;
    background:
      radial-gradient(ellipse 60% 22% at 45% 72%, rgba(255,170,70,.95), rgba(255,120,40,.5) 45%, transparent 75%),
      linear-gradient(180deg, #1d6fc0 0%, #3a8ad0 22%, #8fb3cf 42%, #c9a98a 56%, #e08a45 66%, #7a5a66 76%, #2b4f86 86%, #16335f 100%);
  }
  .front-boat-photo {
    position: absolute; left: 204px; top: 0; width: 222px; height: 134px;
    background: linear-gradient(160deg, #5d8fbe, #2f5f95 60%, #8fb0cc);
    border-bottom-left-radius: 60% 40%;
    opacity: .9;
  }
  .front-sail-photo {
    position: absolute; left: 320px; top: 210px; width: 106px; height: 300px;
    background: linear-gradient(180deg, rgba(230,235,240,.7), rgba(180,195,210,.4));
    border-top-left-radius: 100% 100%;
  }
  .front-wave {
    position: absolute; right: -40px; top: -20px; width: 160px; height: 990px;
    border-left: 46px solid rgba(14,80,160,.75);
    border-radius: 60% 0 0 60% / 50% 0 0 50%;
  }
  .brand-mark {
    position: absolute; left: 40px; top: 112px;
    display: flex; align-items: center; gap: 12px;
  }
  .brand-mark__dot { width: 26px; height: 26px; border-radius: 50%; background: var(--brand-red); }
  .brand-mark__name {
    font-family: "Raleway", sans-serif; font-weight: 800; font-size: 44px;
    color: var(--brand-blue); letter-spacing: 0.5px; white-space: nowrap;
  }
  .front-headline {
    position: absolute; right: 135px; top: 234px;
    font-family: "Raleway", sans-serif; font-weight: 700; font-size: 25px; line-height: 27.7px;
    color: var(--headline-blue); text-align: right; letter-spacing: -0.6px; white-space: nowrap;
  }
  .front-body {
    position: absolute; left: 144px; top: 410px;
    font-family: "Raleway", sans-serif; font-weight: 400; font-size: 15.4px; line-height: 17.9px;
    color: var(--ink); letter-spacing: -0.4px; white-space: nowrap;
  }
  .front-body strong { font-weight: 800; }
  .front-url {
    position: absolute; left: 0; right: 0; top: 868px; text-align: center;
    font-family: "Raleway", sans-serif; font-weight: 400; font-size: 29px; color: #fff;
  }

  /* BACK */
  .back-bg {
    position: absolute; inset: 0;
    background:
      radial-gradient(ellipse 70% 55% at 45% 50%, rgba(255,255,255,.95), rgba(230,238,250,.75) 55%, transparent 85%),
      linear-gradient(180deg, #3f86d6 0%, #8fb8e6 14%, #e6eef9 40%, #dfe9f7 70%, #6f9fd8 92%, #3d6fb8 100%);
  }
  .trip-title {
    position: absolute; left: 37px; top: 32px;
    font-family: "Oswald", sans-serif; font-weight: 500; font-size: 27px; color: #fff;
  }
  .trip-intro {
    position: absolute; left: 37px; top: 74px;
    font-family: "Roboto Condensed", sans-serif; font-weight: 700; font-size: 12.6px; line-height: 14.3px;
    color: var(--ink); letter-spacing: -0.45px; white-space: nowrap;
  }
  .service__title {
    position: absolute; font-family: "Roboto Condensed", sans-serif; font-weight: 700; font-size: 20px;
  }
  .service__text {
    position: absolute; font-family: "Raleway", sans-serif; font-weight: 400; font-size: 12.6px; line-height: 16px;
    color: var(--ink-soft); letter-spacing: -0.2px;
  }
  .service__title--blast { left: 55px; top: 236px; color: #a8232a; }
  .service__text--blast { left: 55px; top: 258px; width: 260px; }
  .service__title--half { left: 148px; top: 314px; color: var(--brand-blue); }
  .service__text--half { left: 148px; top: 339px; width: 262px; }
  .service__title--full { left: 55px; top: 408px; color: var(--teal); }
  .service__text--full { left: 55px; top: 431px; width: 262px; }
  .service__title--custom { left: 53px; top: 476px; color: var(--coral); font-size: 21px; }
  .service__text--custom { left: 53px; top: 505px; width: 352px; font-size: 11.6px; }
  .route-map {
    position: absolute; width: 78px; height: 78px;
    background: linear-gradient(135deg, #cfe2f5, #9cc3ea 55%, #dfe8d6);
  }
  .route-map--blast { left: 318px; top: 237px; }
  .route-map--half { left: 55px; top: 320px; }
  .route-map--full { left: 315px; top: 398px; }
  .safety {
    position: absolute; left: 37px; top: 560px;
    font-family: "Raleway", sans-serif; font-weight: 400; font-size: 11.2px; line-height: 15.8px;
    color: var(--ink-soft); letter-spacing: -0.3px; white-space: nowrap;
  }
  .kids-photo {
    position: absolute; left: 266px; top: 614px; width: 158px; height: 147px;
    border-radius: 100% 0 0 0 / 100% 0 0 0;
    background: linear-gradient(160deg, #8fb8e0, #3a5f95 45%, #c23a3a 80%, #7a2a30);
  }
  .back-brand { left: 44px; top: 696px; gap: 10px; }
  .back-brand .brand-mark__name { font-size: 34px; }
  .back-brand .brand-mark__dot { width: 20px; height: 20px; }
  .boat-notes {
    position: absolute; left: 37px; top: 776px; width: 362px;
    font-family: "Roboto Condensed", sans-serif; font-size: 8.3px; line-height: 12px;
    color: #f4f6fb; letter-spacing: -0.2px;
  }
  .contact-address {
    position: absolute; left: 37px; top: 861px;
    font-family: "Raleway", sans-serif; font-size: 12px; color: #fff;
  }
  .contact-line {
    position: absolute; left: 37px;
    font-family: "Raleway", sans-serif; font-weight: 800; font-size: 16px; color: var(--navy);
  }
  .contact-line--email { top: 878px; }
  .contact-line--phone { top: 896px; }
  .social-square {
    position: absolute; left: 310px; top: 876px; width: 27px; height: 28px; border-radius: 3px;
    background: #3b5da8;
  }
  .license-badge {
    position: absolute; left: 347px; top: 858px; width: 53px; height: 53px; border-radius: 50%;
    background: #1f3f8c; border: 3px solid #d9b24a;
  }
</style>
</head>
<body>
<main class="stage">

  <section class="card card--front">
    <div class="front-scene" role="img" aria-label="Photo of a sailboat deck at sunset over San Francisco Bay"></div>
    <div class="front-boat-photo" role="img" aria-label="Photo of the cruising boat docked at the marina"></div>
    <div class="front-sail-photo" role="img" aria-label="Photo of a sailboat under sail on the bay"></div>
    <div class="front-wave"></div>

    <div class="brand-mark">
      <span class="brand-mark__dot"></span>
      <span class="brand-mark__name">Tidewren</span>
    </div>

    <h1 class="front-headline">Come aboard the<br>amazing Tidewren<br>and experience the<br>spectacular views of<br>San Francisco and<br>the rest of the bay</h1>

    <p class="front-body">Tidewren is a supreme blue-water<br>cruising boat with all the modern<br>safety, comfort and entertainment<br>equipment you would expect.<br>Your time aboard Tidewren is<br>yours to enjoy and direct as you<br>wish while we show you San<br>Francisco Bay, the Golden Gate<br>Bridge, Alcatraz, Treasure and<br>Angel Islands and so much more.<br>We love to show families how to<br>sail and have great fun on the<br>water <strong>while staying safe.</strong></p>

    <p class="front-url">www.tidewren.com</p>
  </section>

  <section class="card card--back">
    <div class="back-bg"></div>

    <h2 class="trip-title">The Trip</h2>
    <p class="trip-intro">Tidewren is located at the Berkeley Marina and perfectly placed to take<br>advantage of the vast and beautiful Bay. Those that live or visit the East<br>Bay or the Central Valley can easily reach the marina and parking is no<br>problem. When chartering Tidewren, the vessel is yours to direct<br>anywhere within the time you wish to enjoy her. We do have a few old<br>favorites that are always fun that we have listed below. These are just to<br>provide an idea of the possible cruise as every trip takes into account<br>your ideas and natures (tides, weather and currents) will. If your looking<br>for something a little different or to mix it up a bit, let us know and we<br>can make it happen. Our custom trips are simple to arrange and book,<br>we simply ask for a minimum of 3 hours duration.</p>

    <h3 class="service__title service__title--blast">2 hour Blast</h3>
    <p class="service__text service__text--blast">Could be a sunset sail, an early morning wake up cruise or a blast out into the bay anytime to find peace, fresh air and amazing views.</p>
    <div class="route-map route-map--blast" role="img" aria-label="Map of the 2 hour route on the bay"></div>

    <div class="route-map route-map--half" role="img" aria-label="Map of the half day route on the bay"></div>
    <h3 class="service__title service__title--half">½ day Fun</h3>
    <p class="service__text service__text--half">A full morning, afternoon or evening out in the Bay seeing many of the main features and landmarks close to the Bay from the water. Actual duration 4-5 hours</p>

    <h3 class="service__title service__title--full">Full Day Adventure</h3>
    <p class="service__text service__text--full">The day includes a complete circuit of the Bay and lunch at anchor. Actual duration 7-8 hours.</p>
    <div class="route-map route-map--full" role="img" aria-label="Map of the full day circuit of the bay"></div>

    <h3 class="service__title service__title--custom">Custom Cruise available</h3>
    <p class="service__text service__text--custom">When booking online just select the day and start time as normal and record the length of trip you are looking for as text in the comments and we will get into contact with you to sort it out.</p>

    <p class="safety">The safety of everyone aboard Tidewren is paramount to our business<br>and your enjoyment. Life preservers are available for all including<br>kids sizes. Children 5 and over are happily encouraged to come<br>along, though children younger are discouraged as parents<br>spend more time keeping their little ones safe than<br>enjoying the sail.</p>

    <div class="kids-photo" role="img" aria-label="Photo of two children in life jackets aboard the boat"></div>

    <div class="brand-mark back-brand">
      <span class="brand-mark__dot"></span>
      <span class="brand-mark__name">Tidewren</span>
    </div>

    <p class="boat-notes">Tidewren is a 50 foot, center cockpit, cutter rigged, mono-hulled, blue water cruising sail boat. What does that mean to you and me... she's a nice sized boat with the driving position and main seats at the center of the boat. She has three positions for sails, main (the big one), jib (front sail) and stay-sail (between main and jib). She has a single hull so will lean over as the wind blows. This is important as this safely removes pressure and force from the rig in heavy weather. The blue water bit just means she was designed to race and cruise long distance and in open oceans.</p>

    <p class="contact-address">Harbor Point Marina, 48 Wharf Road, Berkeley, CA 94710</p>
    <p class="contact-line contact-line--email">e: Bookings@Tidewren.com</p>
    <p class="contact-line contact-line--phone">Call: (510) 555-SAIL (7245)</p>
    <span class="social-square"></span>
    <span class="license-badge"></span>
  </section>

</main>
</body>
</html>
```